Newsletter Banner for email based newsletter

Newsletter banner with Brintak as the main focus and our other 2 companies Tollwyn and Quendar Specialists, included. 72 dpi and in RGB color mode, the banner should be the same dimensions as the attached example (BrintakNewsHeader2). I have also attached the Brintak and other logos. Note as soon as we receive a decent banner we will accept it as the period for this is only 1 day.

```html
<!DOCTYPE html>
<html lang="en">
<head>
<meta charset="utf-8">
<title>Brintak Newsletter Banner</title>
<link href="https://fonts.googleapis.com/css2?family=Arimo:wght@400;700&display=swap" rel="stylesheet">
<style>
  :root {
    --navy: #1d3c6e;
    --grey: #7d8590;
    --white: #ffffff;
    --orange: #f39a2b;
    --fire-dark: #3a1d0e;
    --fire-glow: #e07a1f;
    --sky: #6d8fb8;
    --field: #3f6a3a;
    --lab-light: #c9ccc8;
    --lab-dark: #4d5550;
  }
  html, body {
    margin: 0;
    padding: 0;
    overflow: hidden;
    background: var(--white);
  }
  .banner {
    position: relative;
    width: 1200px;
    height: 214px;
    overflow: hidden;
    font-family: "Arimo", Arial, sans-serif;
    background: var(--white);
  }
  .photo {
    position: absolute;
    top: 0;
    height: 214px;
  }
  .photo--fire-test {
    left: 320px;
    width: 323px;
    background: radial-gradient(ellipse at 60% 70%, var(--fire-glow) 0%, #a0461a 30%, var(--fire-dark) 75%);
  }
  .photo--antenna {
    left: 645px;
    width: 226px;
    background: linear-gradient(180deg, var(--sky) 0%, #9db7d2 55%, var(--field) 72%, #2e4f2b 100%);
  }
  .photo--lab {
    left: 873px;
    width: 258px;
    background: linear-gradient(135deg, var(--lab-light) 0%, #a7aca6 45%, var(--lab-dark) 100%);
  }
  .newsletter-tab {
    position: absolute;
    left: 1131px;
    top: 0;
    width: 69px;
    height: 214px;
    background: var(--orange);
    display: flex;
    align-items: center;
    justify-content: center;
  }
  .newsletter-tab span {
    transform: rotate(-90deg);
    color: var(--white);
    font-weight: 700;
    font-size: 22px;
    letter-spacing: 2px;
    white-space: nowrap;
  }
  .brand-panel {
    position: absolute;
    left: 0;
    top: 0;
  }
  .brand-main {
    position: absolute;
    left: 22px;
    top: 34px;
    display: flex;
    align-items: center;
  }
  .brand-mark {
    width: 52px;
    height: 52px;
    background: var(--navy);
    margin-right: 14px;
  }
  .brand-name {
    color: var(--navy);
    font-weight: 700;
    font-size: 50px;
    line-height: 1;
    letter-spacing: 1px;
  }
  .brand-sub {
    position: absolute;
    left: 220px;
    top: 90px;
    color: var(--navy);
    font-size: 17px;
  }
  .sister-brand {
    position: absolute;
    top: 118px;
    font-size: 27px;
    line-height: 24px;
  }
  .sister-brand--quendar {
    left: 20px;
    color: var(--navy);
  }
  .sister-brand--tollwyn {
    left: 192px;
    color: var(--grey);
  }
</style>
</head>
<body>
  <div class="banner">
    <div class="photo photo--fire-test" role="img" aria-label="Fire test in a laboratory with bright orange flames"></div>
    <div class="photo photo--antenna" role="img" aria-label="Red log-periodic antenna on a mast against blue sky and trees"></div>
    <div class="photo photo--lab" role="img" aria-label="Laboratory testing machine close-up"></div>

    <svg class="brand-panel" width="360" height="214" viewBox="0 0 360 214" aria-hidden="true">
      <path d="M0 0 H338 Q362 107 346 214 H0 Z" fill="var(--white)"/>
    </svg>

    <div class="brand-main">
      <div class="brand-mark"></div>
      <div class="brand-name">BRINTAK</div>
    </div>
    <div class="brand-sub">Laboratories</div>

    <div class="sister-brand sister-brand--quendar">quendar<br>specialists</div>
    <div class="sister-brand sister-brand--tollwyn">tollwyn<br>laboratories</div>

    <div class="newsletter-tab"><span>NEWSLETTER</span></div>
  </div>
</body>
</html>
```